Web page design for Stride Foot Clinic*

Need a web page for our Stride Foot Clinic. It should feature most of our services, hours, directions and location. Should include a short bio of the doctor and a contact page.

Coding

Coded - Design and coding required

Number of Pages Required

1 page

Colors

Designer to choose colors to be used in the design.

```html
<!DOCTYPE html>
<html lang="en">
<head>
<meta charset="utf-8">
<title>Stride Foot Clinic</title>
<link href="https://fonts.googleapis.com/css2?family=Raleway:wght@300;400;600;700;800&family=Lato:wght@400;700&display=swap" rel="stylesheet">
<style>
:root{
  --brand:#0a9ae0;
  --navy:#143f90;
  --ink:#333333;
  --body:#555555;
  --soft:#f2f2f2;
  --white:#ffffff;
  --line:#dcdcdc;
}
*{margin:0;padding:0;box-sizing:border-box}
html,body{width:1200px;height:3901px;overflow:hidden;background:var(--white)}
body{position:relative;font-family:'Lato',sans-serif;color:var(--body)}
.abs{position:absolute}
.heading{font-family:'Raleway',sans-serif;color:var(--ink);font-weight:300;letter-spacing:.5px}
.heading b{font-weight:700}
.center{left:0;width:1200px;text-align:center}
.lead{font-size:12px;line-height:20px;color:var(--body)}

/* header */
.site-header{top:0;left:0;width:1200px;height:74px;background:var(--white)}
.logo{left:164px;top:27px;font-family:'Lato',sans-serif;font-weight:700;font-size:21px;color:var(--navy);letter-spacing:.2px}
.nav{right:162px;top:34px;display:flex;gap:33px;font-family:'Raleway',sans-serif;font-size:11.5px;font-weight:600;color:#555}
.nav .active{color:var(--navy)}

/* hero */
.hero{top:74px;left:0;width:1200px;height:638px;background:linear-gradient(100deg,#3f8a2a 0%,#64ad3a 40%,#9dc76c 65%,#d9c1a7 78%,#6ea445 100%)}
.hero-title{left:164px;top:262px;font-family:'Raleway',sans-serif;font-weight:700;font-size:44px;line-height:53px;color:var(--white)}
.hero-text{left:164px;top:376px;width:460px;font-size:11.5px;line-height:19.5px;color:var(--white)}

/* info boxes */
.info{top:579px;width:292px;height:262px;color:var(--white);text-align:center}
.info.hours{left:162px;background:var(--brand)}
.info.phone{left:454px;background:var(--navy)}
.info.direction{left:746px;background:var(--brand)}
.info svg{position:absolute;top:46px;left:116px}
.info-title{position:absolute;top:120px;left:0;width:100%;font-family:'Raleway',sans-serif;font-weight:700;font-size:13px}
.hours-table{position:absolute;top:146px;left:28px;font-size:11px;line-height:23px;text-align:left}
.hours-table span{display:inline-block;width:120px}
.phone-number{position:absolute;top:146px;left:0;width:100%;font-size:23px}
.phone-sub{position:absolute;top:182px;left:0;width:100%;font-size:11px}
.direction-text{position:absolute;top:146px;left:30px;width:232px;font-size:11px;line-height:23px}
.direction-text u{display:block}

/* welcome */
.welcome-title{top:926px;font-size:40px}
.welcome-text{top:988px;left:272px;width:656px;text-align:center}
.btn{display:block;text-align:center;background:var(--navy);color:var(--white);font-size:11px;font-weight:700;border-radius:22px;font-family:'Lato',sans-serif}
.welcome-btn{left:532px;top:1070px;width:135px;height:40px;line-height:40px}

/* services */
.services{top:1201px;left:0;width:1200px;height:1452px;background:var(--soft)}
.services-title{top:1284px;font-size:40px}
.services-sub{top:1334px;left:328px;width:544px;text-align:center}
.service-photo{width:336px;height:336px;border-radius:50%}
.photo-1{left:218px;top:1417px;background:linear-gradient(135deg,#e9e6e1,#d8c2ac 55%,#b9c6d4);box-shadow:4px 6px 0 0 var(--brand)}
.photo-2{left:630px;top:1812px;background:linear-gradient(135deg,#e7ecef,#dbc1aa 55%,#9fb2c3);box-shadow:4px 6px 0 0 var(--navy)}
.photo-3{left:218px;top:2221px;background:linear-gradient(135deg,#7a5538,#b98d68 55%,#e6cfb9);box-shadow:4px 6px 0 0 var(--brand)}
.service-title{font-size:30px}
.rule{width:92px;height:3px;background:var(--brand)}
.rule.navy{background:var(--navy)}
.service-text{width:335px;font-size:12px;line-height:19.5px}

/* team */
.team{top:2653px;left:0;width:1200px;height:533px;background:linear-gradient(180deg,#3c68b3 0%,#2f5aa8 55%,#4470b5 100%)}
.team-title{top:2720px;font-size:40px;color:var(--white)}
.team-sub{top:2770px;left:328px;width:544px;text-align:center;color:var(--white)}
.member{top:2848px;width:195px;height:247px;background:var(--white);text-align:center}
.member .portrait{position:absolute;top:0;left:0;width:100%;height:186px;background:linear-gradient(180deg,#e9eef2,#cfd8e0)}
.member .name{position:absolute;top:202px;left:0;width:100%;font-family:'Raleway',sans-serif;font-weight:700;font-size:15px;color:var(--ink)}
.member .role{position:absolute;top:222px;left:0;width:100%;font-size:11px;color:var(--brand)}
.member.featured{background:rgba(10,154,224,.85)}
.member.featured .portrait{background:transparent}
.member.featured .name,.member.featured .role{color:rgba(255,255,255,.25)}
.overlay-name{position:absolute;top:52px;left:0;width:100%;font-family:'Raleway',sans-serif;font-weight:700;font-size:14px;color:var(--white)}
.overlay-role{position:absolute;top:70px;left:0;width:100%;font-size:11px;color:var(--white)}
.overlay-text{position:absolute;top:96px;left:15px;width:165px;font-size:11px;line-height:19.5px;color:var(--white)}
.overlay-plus{position:absolute;top:166px;left:81px;width:34px;height:34px;border-radius:50%;background:var(--white);color:var(--navy);font-size:24px;line-height:32px}

/* contact */
.contact-title{top:3268px;font-size:40px}
.contact-sub{top:3317px;left:328px;width:544px;text-align:center}
.field{border:1px solid var(--line);background:var(--white);font-size:11px;color:#666;padding:10px}
.send-btn{left:521px;top:3516px;width:156px;height:40px;line-height:40px}

/* footer */
.site-footer{top:3647px;left:0;width:1200px;height:254px;background:var(--brand);color:var(--white)}
.footer-logo{left:164px;top:3702px;font-family:'Lato',sans-serif;font-weight:700;font-size:18px;color:var(--white)}
.social{top:3740px;left:203px;display:flex;gap:10px}
.social span{width:28px;height:28px;border:1.5px solid var(--white);border-radius:50%}
.copyright{left:164px;top:3787px;width:186px;text-align:center;font-size:10.5px;line-height:19px;color:var(--white)}
.footer-head{top:3703px;font-family:'Raleway',sans-serif;font-weight:700;font-size:12px;color:var(--white)}
.footer-list{font-size:11px;line-height:26.5px;list-style:none;color:var(--white)}
.contact-line{font-size:11px;line-height:17px;display:flex;gap:8px;color:var(--white)}
.footer-hours{font-size:10.5px;line-height:23px;color:var(--white)}
.footer-hours span{display:inline-block;width:94px}
</style>
</head>
<body>

<header class="abs site-header">
  <div class="abs logo">Stride Foot Clinic</div>
  <nav class="abs nav">
    <span class="active">HOME</span><span>ABOUT</span><span>SERVICES</span><span>OUR TEAM</span><span>CONTACT</span>
  </nav>
</header>

<section class="abs hero" role="img" aria-label="Photograph of a bare foot stepping on green grass"></section>
<h1 class="abs hero-title">LOREM IPSUM IS<br>SIMPLY DUMMY TEXT</h1>
<p class="abs hero-text">Lorem Ipsum is simply dummy text of the printing and typesetting industry. Lorem Ipsum has been the industry's standard dummy text ever since the 1500s, when an unknown printer took a galley of type and scrambled it to make a type specimen book</p>

<div class="abs info hours">
  <svg width="60" height="60" viewBox="0 0 60 60" fill="none" stroke="#fff" stroke-width="2.5"><circle cx="30" cy="30" r="27"/><path d="M30 13v18l11 8" stroke-linecap="round"/></svg>
  <div class="info-title">OPENING HOURS</div>
  <div class="hours-table">
    <div><span>Monday to Friday</span>10.00 am to 7.00 pm</div>
    <div><span>Saturday</span>11.00 am to 5.00 pm</div>
    <div><span>Sunday</span>Closed</div>
  </div>
</div>
<div class="abs info phone">
  <svg width="60" height="60" viewBox="0 0 60 60" fill="none" stroke="#fff" stroke-width="2.5"><circle cx="30" cy="30" r="27"/><path d="M20 16c-3 2-4 6-2 10 4 8 10 14 18 18 4 2 8 1 10-2l-6-6-4 3c-4-2-8-6-10-10l3-4z" stroke-linejoin="round"/></svg>
  <div class="info-title">PHONE</div>
  <div class="phone-number">123 456 7890</div>
  <div class="phone-sub">CALL US</div>
</div>
<div class="abs info direction">
  <svg width="60" height="60" viewBox="0 0 60 60" fill="none" stroke="#fff" stroke-width="2.5" stroke-linejoin="round"><path d="M8 22l12-5 10 5 12-5v36l-12 5-10-5-12 5z"/><path d="M20 17v36M30 22v36"/><path d="M42 4c-6 0-9 4-9 8 0 6 9 15 9 15s9-9 9-15c0-4-3-8-9-8z" fill="#0a9ae0"/><circle cx="42" cy="12" r="3"/></svg>
  <div class="info-title">GET DIRECTION</div>
  <div class="direction-text">Lorem Ipsum is simply dummy text of the printing and typesettinh.<u>VIEW MAP</u></div>
</div>

<h2 class="abs heading center welcome-title">WELCOME TO <b>STRIDE FOOT CLINIC</b></h2>
<p class="abs lead welcome-text">Lorem Ipsum is simply dummy text of the printing and typesetting industry. Lorem Ipsum has been the industry's standard dummy text ever since the 1500s, when an unknown printer took a galley of type and scrambled it to make a type specimen book. It has survived not only five centuries, but also the leap into electronic typesetting.</p>
<span class="abs btn welcome-btn">CONTACT US</span>

<section class="abs services"></section>
<h2 class="abs heading center services-title">OUR <b>SERVICES</b></h2>
<p class="abs lead services-sub">Lorem Ipsum is simply dummy text of the printing and typesetting industry. Lorem Ipsum has been the industry's standard dummy text ever since the 1500.</p>

<div class="abs service-photo photo-1" role="img" aria-label="Gloved hands examining the sole of a patient's foot"></div>
<h3 class="abs heading service-title" style="left:624px;top:1478px">GENERAL <b>TREATMENT</b></h3>
<div class="abs rule" style="left:624px;top:1523px"></div>
<p class="abs service-text" style="left:624px;top:1545px">Lorem Ipsum is simply dummy text of the printing and typesetting industry. Lorem Ipsum has been the industry's standard dummy text ever since the 1500s, when an unknown printer took a galley of type and scrambled it to make a type specimen book. It has survived not only five centuries, but also the leap into electronic typesetting, remaining essentially unchanged.</p>

<div class="abs service-photo photo-2" role="img" aria-label="Podiatrist treating a patient's foot with a handheld tool"></div>
<h3 class="abs heading service-title" style="left:164px;top:1878px">SPECIALISED <b>TREATMENT</b></h3>
<div class="abs rule navy" style="left:164px;top:1922px"></div>
<p class="abs service-text" style="left:164px;top:1944px">Lorem Ipsum is simply dummy text of the printing and typesetting industry. Lorem Ipsum has been the industry's standard dummy text ever since the 1500s, when an unknown printer took a galley of type and scrambled it to make a type specimen book. It has survived not only five centuries, but also the leap into electronic typesetting, remaining essentially unchanged.</p>

<div class="abs service-photo photo-3" role="img" aria-label="Runner wrapping an injured foot beside sports shoes on a wooden floor"></div>
<h3 class="abs heading service-title" style="left:624px;top:2280px">SPORTS <b>INJURY</b></h3>
<div class="abs rule" style="left:624px;top:2324px"></div>
<p class="abs service-text" style="left:624px;top:2348px">Lorem Ipsum is simply dummy text of the printing and typesetting industry. Lorem Ipsum has been the industry's standard dummy text ever since the 1500s, when an unknown printer took a galley of type and scrambled it to make a type specimen book. It has survived not only five centuries, but also the leap into electronic typesetting, remaining essentially unchanged.</p>

<section class="abs team" role="img" aria-label="Blue-tinted background photograph of feet"></section>
<h2 class="abs heading center team-title">OUR <b>TEAM</b></h2>
<p class="abs lead team-sub">Lorem Ipsum is simply dummy text of the printing and typesetting industry. Lorem Ipsum has been the industry's standard dummy text ever since the 1500.</p>

<div class="abs member" style="left:162px">
  <div class="portrait" role="img" aria-label="Portrait of a doctor in a white coat"></div>
  <div class="name">DOCTOR NAME</div><div class="role">Position</div>
</div>
<div class="abs member featured" style="left:388px">
  <div class="portrait" role="img" aria-label="Portrait of a doctor under a blue overlay"></div>
  <div class="overlay-name">DOCTOR NAME</div>
  <div class="overlay-role">Position</div>
  <div class="overlay-text">Lorem Ipsum is simply dummy text of the printing and typesetting industry.</div>
  <div class="overlay-plus">+</div>
  <div class="name">DOCTOR NAME</div><div class="role">Position</div>
</div>
<div class="abs member" style="left:615px">
  <div class="portrait" role="img" aria-label="Portrait of a doctor in a white coat"></div>
  <div class="name">DOCTOR NAME</div><div class="role">Position</div>
</div>
<div class="abs member" style="left:844px">
  <div class="portrait" role="img" aria-label="Portrait of a doctor in a white coat"></div>
  <div class="name">DOCTOR NAME</div><div class="role">Position</div>
</div>

<h2 class="abs heading center contact-title">CONTACT <b>US</b></h2>
<p class="abs lead contact-sub">Lorem Ipsum is simply dummy text of the printing and typesetting industry. Lorem Ipsum has been the industry's standard dummy text ever since the 1500.</p>
<div class="abs field" style="left:333px;top:3380px;width:240px;height:36px">Name</div>
<div class="abs field" style="left:333px;top:3424px;width:240px;height:36px">Email</div>
<div class="abs field" style="left:333px;top:3469px;width:240px;height:36px">Contact No.</div>
<div class="abs field" style="left:582px;top:3380px;width:283px;height:125px">Message</div>
<span class="abs btn send-btn">SEND MESSAGE</span>

<footer class="abs site-footer"></footer>
<div class="abs footer-logo">Stride Foot Clinic</div>
<div class="abs social"><span></span><span></span><span></span></div>
<p class="abs copyright">© Stride Foot Clinic - 2019. All Rights Reserved.</p>

<div class="abs footer-head" style="left:389px">USEFUL LINKS</div>
<ul class="abs footer-list" style="left:389px;top:3726px">
  <li>Home</li><li>About</li><li>Services</li><li>Our Team</li><li>Contact</li>
</ul>

<div class="abs footer-head" style="left:617px">CONTACT INFO</div>
<div class="abs contact-line" style="left:617px;top:3732px;width:200px">
  <svg width="9" height="13" viewBox="0 0 9 13"><path d="M4.5 0C2 0 0 2 0 4.5 0 8 4.5 13 4.5 13S9 8 9 4.5C9 2 7 0 4.5 0z" fill="#fff"/><circle cx="4.5" cy="4.5" r="1.6" fill="#0a9ae0"/></svg>
  <span>Lorem Ipsum is simply dummy text of the printing</span>
</div>
<div class="abs contact-line" style="left:617px;top:3785px">
  <svg width="11" height="11" viewBox="0 0 11 11"><path d="M2 0C0 1 0 3 1.5 5.5 3 8 5 10 7.5 10.5 9 11 10.5 10 11 9L9 7 7.5 8C6 7.5 4 5.5 3.5 4L4.5 2.5z" fill="#fff"/></svg>
  <span>123 456 7890</span>
</div>
<div class="abs contact-line" style="left:617px;top:3821px">
  <svg width="12" height="10" viewBox="0 0 12 10"><rect width="12" height="10" rx="1" fill="#fff"/><path d="M0.5 1l5.5 4.5L11.5 1" fill="none" stroke="#0a9ae0" stroke-width="1.2"/></svg>
  <span>hello@stridefootclinic.com</span>
</div>

<div class="abs footer-head" style="left:845px">OPENING HOURS</div>
<div class="abs footer-hours" style="left:845px;top:3728px">
  <div><span>Monday to Friday</span>10.00 am to 7.00 pm</div>
  <div><span>Saturday</span>11.00 am to 5.00 pm</div>
  <div><span>Sunday</span>Closed</div>
</div>

</body>
</html>
```